Harborline Talent Web Site

I would like to change our current website to a better design. www.harborlinetalent.net.
Use the content from the this website.
Updates
The web site is down until 7AM EST on 3/25 for server maintenance. Sorry for the inconvenience.
REMEMBER: I am changing the website to focus on science and technical jobs across all industries. So, if your images focus on only biotech or only DNA or beakers that will not serve Aerospace very well or curcuit board manufacturing. So, either use a montage of images that cover everything or make you images more abstract.
Target Market(s)
We are now staffing for all science and technical jobs. Not just biotech and pharmaceutical.
So, pharmaceutical, biotech, aerospace, alternative energy, research, medical...etc. Anyone with a science or tehcnical background.
Number of Pages Required
5+ pages
Requirements
Must have
- Tag line: "The Science of Recruiting" replaces "A pharmaceutical and bitech search firm"
Pictures and images across more industries.
The job serach page only needs a banner. That page is being worked internally.

```html
<!DOCTYPE html>
<html lang="en">
<head>
<meta charset="utf-8">
<title>Harborline Talent – Home and Inner Page</title>
<link rel="stylesheet" href="https://fonts.googleapis.com/css2?family=Archivo+Black&family=Questrial&family=Open+Sans:wght@400;700&display=swap">
<style>
:root{
  --board:#ffffff;
  --band-dark:#2b2b2b;
  --band-mid:#565656;
  --page-bg:#f4f4f4;
  --header-bg:#efefef;
  --nav-bg:#3b3b3b;
  --nav-text:#f2f2f2;
  --orange:#b46e17;
  --orange-light:#e09a2c;
  --orange-dark:#7a4608;
  --panel-dark:#333333;
  --green:#1f5a1f;
  --field-green:#0f8f0f;
  --field-green-dark:#0a6e0a;
  --text:#3f3f3f;
  --text-strong:#222222;
  --orange-text:#d9861c;
  --rule:#c9c9c9;
  --footer-bg:#3a3a3a;
}
*{box-sizing:border-box;margin:0;padding:0}
html,body{width:1200px;height:2950px;overflow:hidden;background:var(--board)}
body{position:relative;font-family:"Open Sans",Arial,sans-serif;color:var(--text)}

.board-label{position:absolute;left:0;width:1200px;text-align:center;font-family:"Archivo Black",Arial,sans-serif;font-size:46px;letter-spacing:2px;color:#000}
.side-band{position:absolute;left:0;width:1200px;height:574px;background:linear-gradient(180deg,var(--band-dark),var(--band-mid))}

.site{position:absolute;left:77px;width:1046px;background:var(--page-bg);overflow:hidden}
.site-header{position:absolute;left:0;top:0;width:1046px;height:150px;background:linear-gradient(180deg,#f7f7f7,var(--header-bg))}
.brand{position:absolute;left:27px;top:76px;font-family:"Questrial",sans-serif;font-size:31px;letter-spacing:1px;color:var(--green);text-transform:uppercase}
.header-photo{position:absolute;right:0;top:0;width:247px;height:150px;background:linear-gradient(180deg,#f4f4f0 0%,#e9ecea 40%,#2f6fd0 45%,#1d54b8 100%)}

.main-nav{position:absolute;left:0;top:150px;width:1046px;height:49px;background:linear-gradient(180deg,#454545,var(--nav-bg))}
.main-nav a{position:absolute;top:0;line-height:49px;font-family:"Questrial",sans-serif;font-size:19px;color:var(--nav-text);text-decoration:none;transform:translateX(-50%);white-space:nowrap}
.main-nav i{position:absolute;top:8px;width:0;height:34px;border-left:1px dotted #8a8a8a}

.hero{position:absolute;left:0;top:199px;width:1046px;background:radial-gradient(ellipse at 70% 40%,var(--orange-light) 0%,var(--orange) 45%,var(--orange-dark) 100%)}
.hero-panel{position:absolute;left:3px;width:428px;background:var(--panel-dark)}
.hero-title{position:absolute;left:24px;font-family:"Questrial",sans-serif;font-size:27px;color:#fff;white-space:nowrap}
.hero-rule{position:absolute;left:24px;top:87px;width:372px;border-top:1px solid #777}
.hero-label{position:absolute;left:24px;top:110px;font-weight:700;font-size:14.5px;letter-spacing:.5px;color:#fff}
.hero-text{position:absolute;left:24px;width:375px;font-weight:700;font-size:12.5px;line-height:19.5px;letter-spacing:.4px;color:#fff}
.read-more{position:absolute;left:263px;top:234px;width:124px;height:23px}
.hero-photo{position:absolute;border:3px solid #f2f2f2;border-radius:6px;box-shadow:0 2px 6px rgba(0,0,0,.35)}
.hero-arrow{position:absolute;width:46px;height:46px}

.divider{position:absolute;width:0;border-left:1px dotted var(--rule)}
.section-title{position:absolute;font-family:"Questrial",sans-serif;font-size:25px;color:#444;white-space:nowrap}
.section-title .name{color:var(--green)}
.section-title .name em{font-style:normal;color:var(--orange-text)}

.field-card{position:absolute;left:26px;width:383px;background:linear-gradient(180deg,var(--field-green),var(--field-green-dark));color:#fff;padding:4px 5px}
.field-card h3{font-size:13px;font-weight:700;letter-spacing:.5px;line-height:16px}
.field-card p{font-size:11.5px;line-height:17px;letter-spacing:.3px}
.field-card b{font-size:10px;display:block;line-height:13px}
.field-card svg{position:absolute;right:10px;top:6px}
.link-more-fields{position:absolute;left:26px;width:383px;text-align:right;font-weight:700;font-size:12.5px;color:#333;text-decoration:underline}

.lead{position:absolute;font-size:13px;line-height:19.5px;color:var(--text)}
.bullets{position:absolute;left:26px;width:385px;list-style:none}
.bullets li{position:relative;padding-left:18px;font-weight:700;font-size:12.5px;line-height:19.5px;color:#333;margin-bottom:19px}
.bullets li::before{content:"»";position:absolute;left:2px;top:-1px;font-size:12px;color:#555}

.intro-sub{position:absolute;left:478px;top:579px;font-weight:700;font-size:12.5px;color:#222}
.intro-text{position:absolute;left:478px;width:540px;font-size:12.8px;line-height:21.7px;color:var(--text)}

.news-item{position:absolute;left:478px;width:535px;border:1px solid #d8d8d8;background:linear-gradient(180deg,#f0f0f0,#f8f8f8)}
.news-thumb{position:absolute;left:14px;top:10px;width:119px;height:75px}
.news-body{position:absolute;left:143px;top:14px;font-size:12px;line-height:19.5px;color:#444}
.news-body strong{color:var(--green);font-size:13px;letter-spacing:.3px}
.news-body .date{font-size:11.5px;color:#555}
.news-more{position:absolute;font-weight:700;font-size:13px;color:#222}

.site-footer{position:absolute;left:3px;width:1040px;background:var(--footer-bg);color:#fff;font-weight:700;font-size:11px;letter-spacing:.2px}
.site-footer .copy{position:absolute;left:23px;top:0}
.site-footer .links{position:absolute;right:26px;top:0}

.portrait{position:absolute;left:26px;top:449px;width:393px;height:663px;border:7px solid #ececec;box-shadow:0 0 0 1px #c9c9c9,0 3px 6px rgba(0,0,0,.25);background:linear-gradient(160deg,#3c3f40 0%,#8a8e90 35%,#c7c9c8 60%,#6e6f70 100%)}
.about{position:absolute;left:478px;top:442px;width:540px}
.about h2{font-family:"Questrial",sans-serif;font-weight:400;font-size:25px;color:#444;margin-bottom:20px}
.about h4{font-size:12.5px;font-weight:700;color:#222;margin-bottom:9px}
.about p{font-size:13px;line-height:15px;color:var(--text);margin-bottom:15px}
.about p.gap{margin-top:34px}
.about h4.gap{margin-top:8px}
</style>
</head>
<body>

<!-- ============ HOME PAGE ============ -->
<div class="board-label" style="top:48px">HOME PAGE</div>
<div class="side-band" style="top:197px"></div>

<div class="site" style="top:197px;height:1283px">
  <header class="site-header">
    <div class="brand">Harborline Talent</div>
    <div class="header-photo" role="img" aria-label="Laboratory beaker with blue liquid and a pipette"></div>
  </header>

  <nav class="main-nav">
    <a style="left:78px">Home</a><i style="left:136px"></i>
    <a style="left:206px">About Us</a><i style="left:276px"></i>
    <a style="left:349px">Expertise</a><i style="left:418px"></i>
    <a style="left:530px">Employer Services</a><i style="left:641px"></i>
    <a style="left:757px">Candidate Services</a><i style="left:872px"></i>
    <a style="left:953px">Contact Us</a>
  </nav>

  <section class="hero" style="height:289px">
    <div class="hero-panel" style="top:7px;height:277px">
      <h1 class="hero-title" style="top:34px">THE SCIENCE OF RECRUITING</h1>
      <div class="hero-rule"></div>
      <div class="hero-label">ALTERNATIVE ENERGY:</div>
      <p class="hero-text" style="top:130px">Lorem Ipsum is simply dummy text of the printing and typesetting industry. Lorem Ipsum has been the industry's standard dummy text ever since the 1500s, when an unknown printer took.</p>
      <svg class="read-more" viewBox="0 0 124 23" aria-label="Read More">
        <path d="M0 0H106L124 11.5L106 23H0Z" fill="#fff"/>
        <path d="M106 0L124 11.5L106 23L112 11.5Z" fill="#bdbdbd"/>
        <text x="14" y="15.5" font-family="Open Sans, sans-serif" font-weight="700" font-size="11.5" fill="#333">Read More</text>
      </svg>
    </div>
    <svg class="hero-arrow" style="left:477px;top:131px" viewBox="0 0 46 46"><circle cx="23" cy="23" r="23" fill="#3a3a3a"/><path d="M26 15L19 23L26 31M33 15L26 23L33 31" stroke="#ddd" stroke-width="3" fill="none"/></svg>
    <div class="hero-photo" style="left:534px;top:32px;width:411px;height:227px;background:linear-gradient(180deg,#d7e6f5 0%,#6f9be0 35%,#2e5fc0 65%,#7f8b3a 88%,#c7b554 100%)" role="img" aria-label="Rows of solar panels under a bright sky"></div>
    <svg class="hero-arrow" style="left:950px;top:131px" viewBox="0 0 46 46"><circle cx="23" cy="23" r="23" fill="#3a3a3a"/><path d="M13 15L20 23L13 31M20 15L27 23L20 31" stroke="#ddd" stroke-width="3" fill="none"/></svg>
  </section>

  <div class="divider" style="left:430px;top:519px;height:681px"></div>

  <h2 class="section-title" style="left:26px;top:528px">Field of Interst:</h2>

  <div class="field-card" style="top:579px;height:75px">
    <h3>AEROSPACE:</h3>
    <p>Lorem Ipsum is simply dummy text<br>of the printing &nbsp;and typesetting industry.</p>
    <b>More</b>
    <svg width="64" height="64" viewBox="0 0 64 64"><path d="M8 12L14 10L36 26L50 12C54 8 60 8 58 14L44 28L56 52L50 54L34 36L22 46L24 54L20 56L14 46L6 42L8 38L16 40L26 28Z" fill="#fff"/></svg>
  </div>
  <div class="field-card" style="top:665px;height:72px">
    <h3>ALTERNATIVE ENERGY:</h3>
    <p>Lorem Ipsum is simply dummy text<br>of the printing and typesetting industry.</p>
    <b>More</b>
    <svg width="64" height="62" viewBox="0 0 64 62"><g fill="none" stroke="#dff5df" stroke-width="1.6"><ellipse cx="32" cy="31" rx="28" ry="10"/><ellipse cx="32" cy="31" rx="28" ry="10" transform="rotate(60 32 31)"/><ellipse cx="32" cy="31" rx="28" ry="10" transform="rotate(-60 32 31)"/></g><circle cx="32" cy="31" r="4" fill="#dff5df"/></svg>
  </div>
  <div class="field-card" style="top:751px;height:72px">
    <h3>ELECTRONICS:</h3>
    <p>Lorem Ipsum is simply dummy text<br>of the printing and typesetting industry.</p>
    <b>More</b>
    <svg width="64" height="64" viewBox="0 0 64 64"><circle cx="32" cy="34" r="27" fill="#fff"/><path d="M42 4L20 34H32L24 62L48 28H36L46 4Z" fill="#0c7d0c" stroke="#fff" stroke-width="2"/></svg>
  </div>
  <div class="link-more-fields" style="top:832px">Click for More fields</div>

  <h2 class="section-title" style="left:26px;top:872px">Our Proposals:</h2>
  <p class="lead" style="left:26px;top:918px;width:385px">Lorem Ipsum is simply dummy text of the printing and typesetting industry. Lorem Ipsum has been the industry's standard dummy text ever since the 1500s.</p>
  <ul class="bullets" style="top:996px">
    <li>Lorem Ipsum is simply dummy text of the printing and typesetting industry.</li>
    <li>Lorem Ipsum is simply dummy text of the printing and typesetting industry.</li>
    <li>Lorem Ipsum is simply dummy text of the printing and typesetting industry.</li>
  </ul>

  <h2 class="section-title" style="left:478px;top:529px">Welcome to <span class="name">Harborline <em>Talent!</em></span></h2>
  <div class="intro-sub">Executive Search, Recruiting and Contract Services</div>
  <p class="intro-text" style="top:612px">Employees are every company's key to success. Harborline Talent is a recruiting and search firm distinctly focused on those industries we know best. We have placed employees at all levels throughout the United States.</p>
  <p class="intro-text" style="top:698px">Our continued success and growth are a result of a consistent high level of service with unparalleled commitment to quality and integrity. We are a partner with our clients who rely on our network of candidates within the industry to help them achieve the next level of excellence.</p>

  <h2 class="section-title" style="left:478px;top:870px">Recent News:</h2>
  <article class="news-item" style="top:922px;height:96px">
    <div class="news-thumb" role="img" aria-label="Glass laboratory vessels with blue liquid" style="background:linear-gradient(135deg,#d9f1f6,#69c2d8 50%,#2a8fb0)"></div>
    <div class="news-body"><strong>Proposal 1:</strong> &nbsp;<span class="date">| &nbsp;March 3, 2010</span><br>Lorem Ipsum is simply dummy text of the printing<br>and typesetting industry.</div>
  </article>
  <article class="news-item" style="top:1026px;height:97px">
    <div class="news-thumb" role="img" aria-label="Molecular model of dark spheres and rods" style="background:linear-gradient(135deg,#ffffff,#d5d5d5 50%,#6f6f6f)"></div>
    <div class="news-body"><strong>Proposal 2:</strong> &nbsp;<span class="date">| &nbsp;March 5, 2010</span><br>Lorem Ipsum is simply dummy text of the printing<br>and typesetting industry.</div>
  </article>
  <div class="news-more" style="left:973px;top:1131px">More</div>

  <footer class="site-footer" style="top:1234px;height:49px;line-height:49px">
    <span class="copy">Copyright 2005,Harborline Talent | All rights reserved</span>
    <span class="links">Home &nbsp;| &nbsp;About Us &nbsp;| &nbsp;Employer Services &nbsp;| &nbsp;Candidate Services &nbsp;| &nbsp;Contact Us</span>
  </footer>
</div>

<!-- ============ INNER PAGE ============ -->
<div class="board-label" style="top:1540px">INNER PAGE</div>
<div class="side-band" style="top:1642px"></div>

<div class="site" style="top:1642px;height:1308px">
  <header class="site-header">
    <div class="brand">Harborline Talent</div>
    <div class="header-photo" role="img" aria-label="Laboratory beaker with blue liquid and a pipette"></div>
  </header>

  <nav class="main-nav">
    <a style="left:78px">Home</a><i style="left:136px"></i>
    <a style="left:206px">About Us</a><i style="left:276px"></i>
    <a style="left:349px">Expertise</a><i style="left:418px"></i>
    <a style="left:530px">Employer Services</a><i style="left:641px"></i>
    <a style="left:757px">Candidate Services</a><i style="left:872px"></i>
    <a style="left:953px">Contact Us</a>
  </nav>

  <section class="hero" style="height:203px">
    <div class="hero-panel" style="top:6px;height:191px">
      <h1 class="hero-title" style="top:34px">THE SCIENCE OF RECRUITING</h1>
      <p class="hero-text" style="top:83px">Lorem Ipsum is simply dummy text of the printing and typesetting industry. Lorem Ipsum has been the industry's standard dummy text ever since the 1500s, when an unknown printer took.</p>
    </div>
    <div class="hero-photo" style="left:554px;top:13px;width:405px;height:176px;background:linear-gradient(120deg,#2b2f38 0%,#6e6a6a 40%,#b9a89c 60%,#d8dde6 100%)" role="img" aria-label="Hands assembling wired electronic components"></div>
  </section>

  <div class="portrait" role="img" aria-label="Scientist in safety glasses working with laboratory glassware"></div>
  <div class="divider" style="left:452px;top:428px;height:730px"></div>

  <section class="about">
    <h2>About Us</h2>
    <h4>Company Background:</h4>
    <p>Harborline Talent was established in 2002 to provide executive and management level staffing services to the pharmaceutical and biotech industries. We serve a broad range of clients, forming a collaborative partnership ensuring that their needs are met.</p>
    <p>Our recruiters are industry experts who have typically worked in or consulted to the industry and understand what makes a successful candidate. Through daily networking and research, our ability to quickly identify highly qualified candidates is unmatched.</p>
    <p class="gap">Candidates trust us! We safeguard your confidentiality in the highest regard. Harborline Talent' assurance is to never disclose information to any firm without permission. Candidates at all levels require a high level of professionalism and dignity while pursuing career goals.</p>
    <h4 class="gap">Our Approach to the Job Search:</h4>
    <p>Harborline Talent is focused on what we know best; Biotech and Pharmaceuticals. We take pride in understanding the position requirements. Our clients are usually looking for that one special candidate with the necessary knowledge base, skill set and experience.</p>
    <p>Harborline Talent recruiters attribute their success to our high level of networking within the industry; employing techniques that gather information from many different sources. We work with our candidates to ensure the best possible fit.</p>
    <p>As your partner, we invest the time to understand each client's values, philosophy, requirements, climate and cultural needs. We identify companies and conduct thorough research to align and match candidates. We contact existing relationships and engage new ones with direct recruiting. We spend quality time to qualify the best candidates, present the opportunity and select those with the right fit. We develop a customized and structured interview to uncover how well each candidate matches up to prioritized job-related competencies. We present candidates for the client to review and interview. If there is not a correct fit, then we continue recruiting.</p>
    <p>We prepare an offer in tandem with the client. We consult with each client, facilitating communication on salary, terms and benefits. After offer acceptance, we assist in the hiring process up to the start date. Induction is critical to ensure collegiality and collaboration during the orientation and beginning stages of an effective working relationship. We maintain contact on both sides to make sure that the outcome of the search assignment meets everyone's expectations.</p>
  </section>

  <footer class="site-footer" style="top:1257px;height:51px;line-height:51px">
    <span class="copy">Copyright 2005,Harborline Talent | All rights reserved</span>
    <span class="links">Home &nbsp;| &nbsp;About Us &nbsp;| &nbsp;Employer Services &nbsp;| &nbsp;Candidate Services &nbsp;| &nbsp;Contact Us</span>
  </footer>
</div>

</body>
</html>
```